Brass Kite Gig - 20 Years of Funk

I'm with a funk band called Brass Kite. We are celebrating our 20 year anniversary with a show on August 3, 2024. We would like some banners made for social media to help promote the gig. I'm attaching some examples of our 10 year anniversary gig so you can at least get an idea of what we are looking for.

Here's the text for the banners:
BRASS KITE Anniversary Gig - 20 Years of Funk!
Saturday, August 10, 2024
with special guest: Marco Delvin
Doors at 7pm, Show at 8pm

We would like three sizes:
1920 x 1005 pixels
1080 x 1080 pixels
1080 x 1920 pixels

You can check out our website for more ideas of our graphic style, etc.. www.brasskiteband.example

```html
<!DOCTYPE html>
<html lang="en">
<head>
<meta charset="utf-8">
<title>Brass Kite Anniversary Gig – Banner Set</title>
<link rel="stylesheet" href="https://fonts.googleapis.com/css2?family=Rammetto+One&family=Oswald:wght@500;700&family=Archivo+Black&display=swap">
<style>
  :root {
    --lime: #c6dc2e;
    --ink: #050505;
    --white: #ffffff;
    --smoke: #9a9a9a;
    --page: #ffffff;
  }
  * { margin: 0; padding: 0; box-sizing: border-box; }
  html, body { width: 1200px; height: 1000px; overflow: hidden; background: var(--page); }
  .board { position: relative; width: 1200px; height: 1000px; }
  .banner { position: absolute; display: block; box-shadow: 0 4px 14px rgba(0,0,0,.25); background: var(--ink); }
  .banner--story { left: 124px; top: 112px; width: 439px; height: 779px; }
  .banner--wide { left: 585px; top: 111px; width: 489px; height: 255px; }
  .banner--square { left: 585px; top: 396px; width: 492px; height: 493px; }

  .display { font-family: "Rammetto One", Georgia, serif; fill: var(--lime); }
  .brand-name { font-family: "Rammetto One", Georgia, serif; fill: var(--lime); }
  .numeral { font-family: "Rammetto One", Georgia, serif; }
  .years { font-family: "Oswald", "Arial Narrow", sans-serif; font-weight: 700; fill: var(--white); }
  .of-funk { font-family: "Oswald", "Arial Narrow", sans-serif; font-weight: 700; fill: var(--lime); }
  .bang { font-family: "Oswald", "Arial Narrow", sans-serif; font-weight: 700; fill: var(--smoke); }
  .info { font-family: "Archivo Black", Arial, sans-serif; fill: var(--white); letter-spacing: .28em; }
  .info .accent { fill: var(--lime); }
  .info .outline-digit { font-family: "Rammetto One", Georgia, serif; fill: none; stroke: var(--white); stroke-width: 1.4; letter-spacing: 0; }
  .guest-label { font-family: "Oswald", "Arial Narrow", sans-serif; font-weight: 500; fill: var(--ink); }
  .guest-name { font-family: "Archivo Black", Arial, sans-serif; fill: var(--ink); }
  .lime-stroke { stroke: var(--lime); fill: none; }
  .lime-fill { fill: var(--lime); }
  .band-strip { fill: var(--lime); }
</style>
</head>
<body>
<main class="board">

  <!-- Story format 1080 x 1920 -->
  <svg class="banner banner--story" viewBox="0 0 768 1364" xmlns="http://www.w3.org/2000/svg">
    <defs>
      <radialGradient id="story-stage" cx="50%" cy="58%" r="60%">
        <stop offset="0" stop-color="#262626"/>
        <stop offset="1" stop-color="#060606"/>
      </radialGradient>
      <linearGradient id="story-beam" x1="0" y1="0" x2="0" y2="1">
        <stop offset="0" stop-color="#ffffff" stop-opacity=".08"/>
        <stop offset="1" stop-color="#ffffff" stop-opacity="0"/>
      </linearGradient>
      <linearGradient id="story-numeral" x1="0" y1="0" x2="1" y2="1">
        <stop offset="0" stop-color="#c8c8c8"/>
        <stop offset=".6" stop-color="#9d9d9d"/>
        <stop offset="1" stop-color="#6a6a6a"/>
      </linearGradient>
    </defs>
    <rect width="768" height="1364" fill="var(--ink)"/>
    <rect y="480" width="768" height="800" fill="url(#story-stage)" role="img" aria-label="Dim black and white photo of the band playing on stage"/>
    <polygon points="120,0 260,0 768,700 768,820" fill="url(#story-beam)"/>
    <polygon points="648,0 508,0 0,700 0,820" fill="url(#story-beam)"/>

    <circle cx="381" cy="155" r="56" stroke-width="12" class="lime-stroke"/>
    <text class="brand-name" x="381" y="161" font-size="16" text-anchor="middle" textLength="82" lengthAdjust="spacingAndGlyphs">Brass Kite</text>

    <text class="display" x="150" y="405" font-size="40" textLength="250" lengthAdjust="spacingAndGlyphs">Brass Kite</text>
    <text class="display" x="238" y="452" font-size="40" textLength="365" lengthAdjust="spacingAndGlyphs">Anniversary Gig</text>

    <g role="img" aria-label="Large numerals 20 filled with a photo of brass players and a trumpeter silhouette">
      <text class="numeral" x="148" y="792" font-size="330" textLength="455" lengthAdjust="spacingAndGlyphs" fill="url(#story-numeral)">20</text>
    </g>

    <text class="years" x="148" y="910" font-size="104" textLength="295" lengthAdjust="spacing">YEARS</text>
    <text class="of-funk" x="463" y="860" font-size="44">OF</text>
    <text class="of-funk" x="463" y="907" font-size="44" textLength="115" lengthAdjust="spacing">FUNK</text>
    <text class="bang" x="585" y="907" font-size="92">!</text>

    <g class="lime-fill" transform="translate(150 1012)">
      <rect width="30" height="28" rx="4" fill="none" stroke="var(--lime)" stroke-width="3"/>
      <rect x="0" y="0" width="30" height="8" rx="3"/>
      <rect x="6" y="-4" width="3" height="7"/><rect x="21" y="-4" width="3" height="7"/>
      <rect x="6" y="13" width="4" height="3"/><rect x="13" y="13" width="4" height="3"/><rect x="20" y="13" width="4" height="3"/>
      <rect x="6" y="19" width="4" height="3"/><rect x="13" y="19" width="4" height="3"/><rect x="20" y="19" width="4" height="3"/>
    </g>
    <text class="info" x="197" y="1044" font-size="21" textLength="406" lengthAdjust="spacing"><tspan class="accent">SATURDAY</tspan>, AUGUST 10, 2024</text>
    <text class="info" x="161" y="1094" font-size="20" textLength="442" lengthAdjust="spacing">DOORS AT <tspan class="outline-digit" font-size="40">7</tspan> PM, SHOW AT <tspan class="outline-digit" font-size="40">8</tspan> PM</text>

    <rect class="band-strip" y="1272" width="768" height="92"/>
    <text class="guest-label" x="162" y="1318" font-size="20">WITH SPECIAL GUEST:</text>
    <text class="guest-name" x="362" y="1320" font-size="30">Marco Delvin</text>
  </svg>

  <!-- Landscape format 1920 x 1005 -->
  <svg class="banner banner--wide" viewBox="0 0 856 447" xmlns="http://www.w3.org/2000/svg">
    <defs>
      <radialGradient id="wide-stage" cx="35%" cy="45%" r="70%">
        <stop offset="0" stop-color="#2c2c2c"/>
        <stop offset="1" stop-color="#070707"/>
      </radialGradient>
      <linearGradient id="wide-numeral" x1="0" y1="0" x2="1" y2="1">
        <stop offset="0" stop-color="#c8c8c8"/>
        <stop offset=".6" stop-color="#9d9d9d"/>
        <stop offset="1" stop-color="#6a6a6a"/>
      </linearGradient>
    </defs>
    <rect width="856" height="447" fill="url(#wide-stage)" role="img" aria-label="Dim black and white photo of the band playing on stage"/>

    <circle cx="62" cy="67" r="34" stroke-width="7" class="lime-stroke"/>
    <text class="brand-name" x="62" y="70" font-size="9" text-anchor="middle" textLength="46" lengthAdjust="spacingAndGlyphs">Brass Kite</text>

    <text class="display" x="175" y="86" font-size="38" textLength="200" lengthAdjust="spacingAndGlyphs">Brass Kite</text>
    <text class="display" x="395" y="86" font-size="38" textLength="410" lengthAdjust="spacingAndGlyphs">Anniversary Gig</text>

    <g role="img" aria-label="Large numerals 20 filled with a photo of brass players and a trumpeter silhouette">
      <text class="numeral" x="168" y="270" font-size="185" textLength="252" lengthAdjust="spacingAndGlyphs" fill="url(#wide-numeral)">20</text>
    </g>

    <text class="years" x="168" y="337" font-size="58" textLength="165" lengthAdjust="spacing">YEARS</text>
    <text class="of-funk" x="345" y="310" font-size="24">OF</text>
    <text class="of-funk" x="345" y="336" font-size="24" textLength="62" lengthAdjust="spacing">FUNK</text>
    <text class="bang" x="412" y="336" font-size="50">!</text>

    <g class="lime-fill" transform="translate(484 166)">
      <rect width="22" height="20" rx="3" fill="none" stroke="var(--lime)" stroke-width="2.5"/>
      <rect width="22" height="6" rx="2"/>
      <rect x="4" y="9" width="3" height="2"/><rect x="9.5" y="9" width="3" height="2"/><rect x="15" y="9" width="3" height="2"/>
      <rect x="4" y="14" width="3" height="2"/><rect x="9.5" y="14" width="3" height="2"/><rect x="15" y="14" width="3" height="2"/>
    </g>
    <text class="info" x="522" y="186" font-size="16"><tspan class="accent">SATURDAY</tspan>,</text>
    <text class="info" x="484" y="217" font-size="16">AUGUST 10, 2024</text>
    <rect x="484" y="243" width="178" height="3" class="lime-fill"/>
    <text class="info" x="484" y="285" font-size="16">DOORS AT <tspan class="outline-digit" font-size="32">7</tspan> PM,</text>
    <text class="info" x="484" y="327" font-size="16">SHOW AT <tspan class="outline-digit" font-size="32">8</tspan> PM</text>

    <path class="band-strip" d="M0 447 C 250 410, 560 390, 856 392 L 856 447 Z"/>
    <text class="guest-label" x="476" y="425" font-size="16">WITH SPECIAL GUEST:</text>
    <text class="guest-name" x="642" y="426" font-size="24">Marco Delvin</text>
  </svg>

  <!-- Square format 1080 x 1080 -->
  <svg class="banner banner--square" viewBox="0 0 862 863" xmlns="http://www.w3.org/2000/svg">
    <defs>
      <radialGradient id="square-stage" cx="50%" cy="55%" r="60%">
        <stop offset="0" stop-color="#262626"/>
        <stop offset="1" stop-color="#060606"/>
      </radialGradient>
      <linearGradient id="square-beam" x1="0" y1="0" x2="0" y2="1">
        <stop offset="0" stop-color="#ffffff" stop-opacity=".09"/>
        <stop offset="1" stop-color="#ffffff" stop-opacity="0"/>
      </linearGradient>
      <linearGradient id="square-numeral" x1="0" y1="0" x2="1" y2="1">
        <stop offset="0" stop-color="#c8c8c8"/>
        <stop offset=".6" stop-color="#9d9d9d"/>
        <stop offset="1" stop-color="#6a6a6a"/>
      </linearGradient>
    </defs>
    <rect width="862" height="863" fill="url(#square-stage)" role="img" aria-label="Dim black and white photo of the band playing on stage"/>
    <polygon points="40,0 200,0 862,560 862,700" fill="url(#square-beam)"/>
    <polygon points="822,0 662,0 0,560 0,700" fill="url(#square-beam)"/>

    <circle cx="430" cy="95" r="47" stroke-width="9" class="lime-stroke"/>
    <text class="brand-name" x="430" y="100" font-size="13" text-anchor="middle" textLength="68" lengthAdjust="spacingAndGlyphs">Brass Kite</text>

    <text class="display" x="218" y="212" font-size="36" textLength="225" lengthAdjust="spacingAndGlyphs">Brass Kite</text>
    <text class="display" x="298" y="252" font-size="36" textLength="340" lengthAdjust="spacingAndGlyphs">Anniversary Gig</text>

    <g role="img" aria-label="Large numerals 20 filled with a photo of brass players and a trumpeter silhouette">
      <text class="numeral" x="215" y="520" font-size="300" textLength="425" lengthAdjust="spacingAndGlyphs" fill="url(#square-numeral)">20</text>
    </g>

    <text class="years" x="215" y="632" font-size="96" textLength="280" lengthAdjust="spacing">YEARS</text>
    <text class="of-funk" x="510" y="586" font-size="40">OF</text>
    <text class="of-funk" x="510" y="630" font-size="40" textLength="108" lengthAdjust="spacing">FUNK</text>
    <text class="bang" x="625" y="630" font-size="84">!</text>

    <g class="lime-fill" transform="translate(218 670)">
      <rect width="27" height="25" rx="4" fill="none" stroke="var(--lime)" stroke-width="3"/>
      <rect width="27" height="7" rx="3"/>
      <rect x="5" y="11" width="4" height="3"/><rect x="11.5" y="11" width="4" height="3"/><rect x="18" y="11" width="4" height="3"/>
      <rect x="5" y="17" width="4" height="3"/><rect x="11.5" y="17" width="4" height="3"/><rect x="18" y="17" width="4" height="3"/>
    </g>
    <text class="info" x="262" y="697" font-size="19" textLength="378" lengthAdjust="spacing"><tspan class="accent">SATURDAY</tspan>, AUGUST 10, 2024</text>
    <text class="info" x="230" y="744" font-size="18" textLength="410" lengthAdjust="spacing">DOORS AT <tspan class="outline-digit" font-size="36">7</tspan> PM, SHOW AT <tspan class="outline-digit" font-size="36">8</tspan> PM</text>

    <rect class="band-strip" y="802" width="862" height="61"/>
    <text class="guest-label" x="230" y="838" font-size="18">WITH SPECIAL GUEST:</text>
    <text class="guest-name" x="415" y="840" font-size="27">Marco Delvin</text>
  </svg>

</main>
</body>
</html>
```